Rovilent.com Trucking Company Website

Need a website designed (no content) for a trucking company, specializing in trucking of ocean containers (intermodal Trucking). Heavy emphasis on technology, using latest technology, providing unabated visibility and realtime information.
clean minimalist industrial website
example:
https://www.belquarn.com/

Target Market(s)

Professional Business Consumer corporate and small business

Industry/Entity Type

Trucking Company

Number of Pages Required

5+ page

Requirements
Must have
• Industrial Design, simple informative, for a busy professional to view and get the necessary information with out the distractions.
• Blog Page
• Client Log-In on the front page
• Technology page - showing our intensive investments in technology
Nice to have
• If ANY images included, MUST be USA related. Example if include an image of a truck, ensure its a USA model. Do the research.
• included our business card for sample of Logo
• Doesnt not have to be the same color schemes.
Should not have
• moving images

```html
<!DOCTYPE html>
<html lang="en">
<head>
<meta charset="utf-8">
<title>Rovilent Consulting – Trucking</title>
<link rel="stylesheet" href="https://fonts.googleapis.com/css2?family=Open+Sans:ital,wght@0,400;0,600;0,700;1,400&display=swap">
<style>
:root{
  --navy:#0b4a80;
  --ink:#111;
  --text:#333;
  --muted:#777;
  --band:#f3f3f3;
  --rule:#c9c9c9;
  --green:#17a05a;
  --footer:#1d1d1d;
  --footer-text:#e6e6e6;
}
*{box-sizing:border-box;margin:0;padding:0}
html,body{width:1200px;height:2228px;overflow:hidden}
body{position:relative;background:#fff;font-family:"Open Sans",Arial,sans-serif;color:var(--text)}
.abs{position:absolute}
a{color:inherit;text-decoration:none}

/* header */
.site-header{left:0;top:0;width:1200px;height:89px;border-bottom:2px solid var(--rule)}
.brand{left:39px;top:14px;line-height:1}
.brand-name{display:block;font-weight:700;font-size:38px;letter-spacing:1px;color:var(--navy)}
.brand-sub{display:block;font-weight:400;font-size:15px;letter-spacing:5px;color:var(--navy);margin-top:2px}
.main-nav{left:518px;top:33px;display:flex;gap:34px;font-size:15px;letter-spacing:.5px;color:var(--ink)}
.nav-login{left:959px;top:28px;width:106px;height:31px;border:1.5px solid #333;border-radius:16px;font-size:13px;display:flex;align-items:center;justify-content:center;color:var(--ink)}

/* hero */
.hero-title{left:107px;top:230px;font-weight:700;font-size:38px;line-height:44px;letter-spacing:2px;color:var(--navy)}
.hero-text{left:107px;top:362px;width:380px;font-size:15px;line-height:18px;letter-spacing:.4px;color:#222}
.btn{display:flex;align-items:center;justify-content:center;font-size:13px;letter-spacing:1px;border-radius:6px}
.btn-outline{left:105px;top:435px;width:128px;height:36px;border:1.5px solid var(--navy);color:var(--navy)}
.btn-solid{left:239px;top:435px;width:128px;height:36px;background:var(--navy);color:#fff}
.hero-photo{left:500px;top:195px;width:650px;height:335px;border-radius:4px;background:linear-gradient(135deg,#f4f4f4 0%,#dcdcdc 45%,#b9bcbf 100%)}
.slider-arrow{top:312px}
.arrow-left{left:18px}
.arrow-right{left:1164px}

/* partners */
.partner-band{left:0;top:587px;width:1200px;height:136px;background:var(--band)}
.partner-badge{top:0}

/* login section */
.section-title{font-weight:700;font-size:30px;letter-spacing:1px;color:var(--navy);text-align:center}
.login-title{left:169px;top:795px;width:300px}
.signup-title{left:720px;top:795px;width:300px}
.divider{left:621px;top:787px;width:2px;height:285px;background:#555}
.field{left:162px;width:307px;height:27px;border-bottom:1.5px solid var(--navy);border-right:1.5px solid var(--navy);font-style:italic;font-size:14px;letter-spacing:.6px;color:#555;padding:5px 0 0 8px}
.field-user{top:898px}
.field-pass{top:946px}
.forgot{left:170px;top:977px;font-size:11px;font-style:italic;color:#6a8fb5;text-decoration:underline}
.btn-login{left:379px;top:1004px;width:90px;height:34px;border-radius:17px;background:var(--navy);color:#fff;font-size:12px}
.benefits{left:708px;top:864px;list-style:none}
.benefits li{display:flex;gap:20px;height:49px;font-size:13.5px;line-height:16px;color:#222}
.benefits svg{flex:none;margin-top:8px}
.btn-signup{left:803px;top:1019px;width:134px;height:50px;border-radius:25px;background:var(--navy);color:#fff;font-size:12px}

/* provide */
.provide-kicker{left:0;top:1166px;width:1200px;text-align:center;font-size:14px;letter-spacing:1px;color:#555}
.provide-title{left:0;top:1180px;width:1200px;text-align:center;font-weight:700;font-size:45px;letter-spacing:1px;color:var(--ink)}
.provide-photo{left:162px;top:1319px;width:442px;height:564px;border-radius:8px;background:linear-gradient(180deg,#a9cbe6 0%,#7aa06a 30%,#2f4a63 55%,#1d2f44 80%,#8b8d8f 100%)}
.feature{left:700px;width:322px;text-align:center}
.feature svg{display:block;margin:0 auto}
.feature-title{font-weight:600;font-size:18.5px;letter-spacing:1.5px;color:var(--navy);margin-top:14px}
.feature-text{font-size:12.5px;line-height:15px;letter-spacing:.5px;color:#888;margin-top:4px}
.f1{top:1346px}
.f2{top:1532px}
.f3{top:1722px}

/* footer */
.site-footer{left:0;top:1945px;width:1200px;height:283px;background:var(--footer);color:var(--footer-text)}
.foot-brand{left:85px;top:48px;line-height:1}
.foot-brand .brand-name{color:#fff;font-size:34px}
.foot-brand .brand-sub{color:#fff;font-size:14px}
.contact{left:85px;top:114px;list-style:none;font-size:13px}
.contact li{display:flex;align-items:center;gap:20px;height:26.5px}
.contact svg{flex:none}
.foot-heading{font-weight:700;font-size:17px;color:#fff;letter-spacing:.5px}
.about-heading{left:397px;top:66px;width:335px;padding-bottom:10px;border-bottom:1.5px solid #777}
.about-text{left:397px;top:124px;width:340px;font-size:12.5px;line-height:26px}
.map-heading{left:803px;top:66px;width:335px;padding-bottom:10px;border-bottom:1.5px solid #777}
.site-map{left:803px;top:118px;display:grid;grid-template-columns:138px 140px;row-gap:17px;font-size:12.5px;list-style:none}
.copyright{left:40px;top:250px;font-size:12px}
</style>
</head>
<body>

<header class="site-header abs">
  <a class="brand abs" href="#"><span class="brand-name">ROVILENT</span><span class="brand-sub">CONSULTING</span></a>
  <nav class="main-nav abs">
    <a href="#">Home</a><a href="#">About us</a><a href="#">Technology</a><a href="#">Blog</a><a href="#">Contact us</a>
  </nav>
  <a class="nav-login abs" href="#">Login</a>
</header>

<section class="hero">
  <svg class="slider-arrow arrow-left abs" width="20" height="30" viewBox="0 0 20 30"><path d="M16 3 L5 15 L16 27" fill="none" stroke="#444" stroke-width="4"/></svg>
  <h1 class="hero-title abs">WE MAKE SHIPPING<br>BIG STUFF EASY</h1>
  <p class="hero-text abs">Join the millions getting bargain deals on shipping cars, furniture, freight, and more...</p>
  <a class="btn btn-outline abs" href="#">LEARN MORE</a>
  <a class="btn btn-solid abs" href="#">LOGIN</a>
  <div class="hero-photo abs" role="img" aria-label="White American semi truck with a long silver trailer"></div>
  <svg class="slider-arrow arrow-right abs" width="20" height="30" viewBox="0 0 20 30"><path d="M4 3 L15 15 L4 27" fill="none" stroke="#444" stroke-width="4"/></svg>
</section>

<section class="partner-band abs" aria-label="Truck manufacturer partners">
  <svg class="partner-badge abs" width="1200" height="136" viewBox="0 0 1200 136">
    <rect x="110" y="52" width="200" height="36" rx="18" fill="#3a3a3a"/>
    <rect x="438" y="56" width="188" height="30" fill="#555"/>
    <rect x="758" y="38" width="52" height="52" transform="rotate(45 784 64)" fill="#4a4a4a"/>
    <ellipse cx="1014" cy="78" rx="72" ry="30" fill="#333"/>
  </svg>
</section>

<section class="login-area">
  <h2 class="section-title login-title abs">USER LOGIN</h2>
  <div class="field field-user abs">Username/E-mail Address</div>
  <div class="field field-pass abs">Login Password</div>
  <a class="forgot abs" href="#">forgot your password?</a>
  <a class="btn btn-login abs" href="#">LOGIN</a>

  <div class="divider abs"></div>

  <h2 class="section-title signup-title abs">BY SIGNING UP</h2>
  <ul class="benefits abs">
    <li><svg width="16" height="12" viewBox="0 0 16 12"><path d="M1 6 L6 10 L15 1" fill="none" stroke="var(--green)" stroke-width="3"/></svg><span>Lorem ipsum dolor sit amet, consectetur<br>adipiscing elit</span></li>
    <li><svg width="16" height="12" viewBox="0 0 16 12"><path d="M1 6 L6 10 L15 1" fill="none" stroke="var(--green)" stroke-width="3"/></svg><span>Lorem ipsum dolor sit amet, consectetur<br>adipiscing elit</span></li>
    <li><svg width="16" height="12" viewBox="0 0 16 12"><path d="M1 6 L6 10 L15 1" fill="none" stroke="var(--green)" stroke-width="3"/></svg><span>Lorem ipsum dolor sit amet, consectetur<br>adipiscing elit</span></li>
  </ul>
  <a class="btn btn-signup abs" href="#">SIGN UP</a>
</section>

<section class="provide">
  <p class="provide-kicker abs">State of the art technology</p>
  <h2 class="provide-title abs">WE PROVIDE</h2>
  <div class="provide-photo abs" role="img" aria-label="Dark blue American long-nose truck with chrome stacks in front of trees"></div>

  <div class="feature f1 abs">
    <svg width="84" height="64" viewBox="0 0 84 64"><rect x="3" y="6" width="48" height="40" fill="none" stroke="#111" stroke-width="3"/><path d="M51 20 H68 L80 34 V46 H51 Z" fill="none" stroke="#111" stroke-width="3"/><circle cx="18" cy="52" r="7" fill="#fff" stroke="#111" stroke-width="3"/><circle cx="66" cy="52" r="7" fill="#fff" stroke="#111" stroke-width="3"/></svg>
    <h3 class="feature-title">LATEST TECHNOLOGY</h3>
    <p class="feature-text">Lorem ipsum dolor sit amet,<br>consectetur adipiscing elit</p>
  </div>
  <div class="feature f2 abs">
    <svg width="90" height="54" viewBox="0 0 90 54"><path d="M3 27 Q45 -12 87 27 Q45 66 3 27 Z" fill="none" stroke="#111" stroke-width="3"/><circle cx="45" cy="27" r="13" fill="none" stroke="#111" stroke-width="3"/><circle cx="45" cy="27" r="6" fill="#111"/></svg>
    <h3 class="feature-title">UNABATED VISIBILITY</h3>
    <p class="feature-text">Lorem ipsum dolor sit amet,<br>consectetur adipiscing elit</p>
  </div>
  <div class="feature f3 abs">
    <svg width="76" height="72" viewBox="0 0 76 72"><circle cx="46" cy="28" r="22" fill="none" stroke="#111" stroke-width="3"/><text x="46" y="35" text-anchor="middle" font-family="Open Sans, sans-serif" font-size="18" font-weight="600" fill="#111">24</text><path d="M8 20 L16 14 L24 26 L19 31 Q24 44 37 50 L42 45 L54 53 L48 61 Q22 60 8 20 Z" fill="none" stroke="#111" stroke-width="3" stroke-linejoin="round"/></svg>
    <h3 class="feature-title">REALTIME INFORMATION</h3>
    <p class="feature-text">Lorem ipsum dolor sit amet,<br>consectetur adipiscing elit</p>
  </div>
</section>

<footer class="site-footer abs">
  <div class="foot-brand abs"><span class="brand-name">ROVILENT</span><span class="brand-sub">CONSULTING</span></div>
  <ul class="contact abs">
    <li><svg width="12" height="16" viewBox="0 0 12 16"><path d="M6 1 A5 5 0 0 1 11 6 C11 10 6 15 6 15 C6 15 1 10 1 6 A5 5 0 0 1 6 1 Z" fill="#fff"/><circle cx="6" cy="6" r="2" fill="var(--footer)"/></svg>48 Harbor Lane, CA 90731</li>
    <li><svg width="12" height="10" viewBox="0 0 12 10"><rect x="0" y="0" width="12" height="10" fill="#fff"/><path d="M0 0 L6 5 L12 0" fill="none" stroke="var(--footer)" stroke-width="1.5"/></svg>info@rovilent.com</li>
    <li><svg width="12" height="12" viewBox="0 0 12 12"><circle cx="6" cy="6" r="5" fill="none" stroke="#fff" stroke-width="1.5"/><path d="M6 3 V6 H8.5" fill="none" stroke="#fff" stroke-width="1.5"/></svg>Monday through Sunday, 24/7</li>
    <li><svg width="12" height="12" viewBox="0 0 12 12"><path d="M1 2 L4 0.5 L6 4 L4.5 5.5 Q5.5 7.5 7 8 L8.5 6.5 L11.5 8.5 L10 11.5 Q2 10 1 2 Z" fill="#fff"/></svg>Call us now: (555) 0142-7788</li>
  </ul>

  <h3 class="foot-heading about-heading abs">ABOUT US</h3>
  <p class="about-text abs">Lorem ipsum dolor sit amet, consectetur adipiscing elit, sed do eiusmod tempor incididunt ut labore et dolore magna aliqua. Ut enim ad minim veniam, quis nostrud exercitation ullamco laboris nisi ut aliquip ex ea commodo consequat.</p>

  <h3 class="foot-heading map-heading abs">SITE MAP</h3>
  <ul class="site-map abs">
    <li><a href="#">Home</a></li><li><a href="#">Blog</a></li>
    <li><a href="#">About us</a></li><li><a href="#">Contact us</a></li>
    <li><a href="#">Technology</a></li><li><a href="#">Privacy/Policy</a></li>
    <li><a href="#">Services</a></li><li><a href="#">FAQ</a></li>
  </ul>

  <p class="copyright abs">© 2017 Rovilent Consulting, Inc. All Rights Reserved</p>
</footer>

</body>
</html>
```